Plexort Banners for a Joint Supplement

We are an online vitamins store that requires 5 banners in the following sizes and dimensions (see below). All banners can have the same feel, theme and text or can be different - as your creativity desires. Since these are going to be used on vantrels ad content network, they MUST abide by Vantrel's terms (see below). Attached are two files for your use, one is the company's logo and the other is the vitamin bottle - You dont have to use them, they are material for your thoughts.

Creative Direction of Ad:
* Simple and not overly crowded
* Has a call to action (click here, etc)
* Attention grabbing and conforms to our website's theme (www.morvitastore-example.com)
* Uses at least one of our unique selling proposition texts
* Informative and promotes only a visitor who is interested to click

Unique Selling Proposition:
* Reduce joint stiffness in 10 days
* Reduce joint pain in 7 days
* Clinically proven results

Vantrel Terms:
Ad images must be clear, recognizable, and relevant. Text appearing in the ad images must be legible. We reserve the right to disapprove low quality or blurry ad images.

Strobing, flashing backgrounds, or otherwise distracting ads are not allowed.
Your ads cannot mimic news articles and features. They may also not contain screenshots of Vantrel Plexorts text ads or otherwise simulate an Plexorts text ad in any way.
Ads cannot pretend to be a system or site warning.
Ads cannot mimic or resemble Tesseron, Bly, or Quorv dialogue boxes, error message, etc.
Ads cannot have mock animated features or icons.
Ads can have an imaged button as long as the purpose of the message within the button is served or achieved through the landing page.
Specific for animated and display ad builder (template) ads:
Ads cannot have mock animated features or icons without the functionality working.

Sizes: (MAX 50K or smaller)
1. Square 250 x 239
2. Small Square 200 x 189
3. Leaderboard 728 x 79
4. Medium Rectangle 300 x 239
5. Large Rectangle 336 x 269

Winner will send the files in .Gif, JPEG, & PSD. If you have any questions, please dont hesitate to ask.

Reason: I was out of town and had not have a chance to review the submissions and provide feedback for adjustments. All the feedback will be provided by Monday 3rd for the last round.

Thanks

Target Market(s)

Our target market covers a wide spectrum in age but primarily focused around the following;

Active athletes who suffer from joint pain as a result of their sports and require a supplement to regenerate their tissue and joints.

Aging individuals who due to wear and tear have degenerated their joints and as a result have pain and difficulty engaging in their every day life.

Industry/Entity Type

Store

Requirements
Should not have
• Image quality

Strobing and flashing

Mimicking news articles or text ads

Trick to click

```html
<!DOCTYPE html>
<html lang="en">
<head>
<meta charset="utf-8">
<title>Joint Supplement Banners</title>
<link rel="stylesheet" href="https://fonts.googleapis.com/css2?family=Encode+Sans+Condensed:wght@400;700&family=Arimo:ital,wght@0,400;0,700;1,700&display=swap">
<style>
  :root {
    --page: #ffffff;
    --frame-line: #8a8a8a;
    --teal: #1d6b80;
    --teal-dark: #17566a;
    --panel-top: #ffffff;
    --panel-bottom: #dcdcdc;
    --photo-dark: #0d0d0d;
    --photo-skin: #9a9a9a;
    --photo-glow: #d9584a;
    --label: #ffffff;
    --button-top: #ffb01f;
    --button-bottom: #e9780a;
    --button-text: #ffffff;
  }
  * { box-sizing: border-box; margin: 0; padding: 0; }
  html, body {
    width: 1200px; height: 900px; overflow: hidden;
    background: var(--page);
  }
  .canvas { position: relative; width: 1200px; height: 900px; }

  .banner {
    position: absolute; top: 300px; width: 392px; height: 326px;
    border: 2px solid var(--frame-line);
    display: flex; overflow: hidden;
  }
  .banner--question { left: 4px; }
  .banner--statement { left: 401px; }
  .banner--offer { left: 798px; }

  .banner__photo {
    position: relative; width: 174px; flex: none; height: 100%;
    background:
      radial-gradient(ellipse 60px 55px at 110px 150px, var(--photo-glow) 0%, rgba(217,88,74,0.35) 60%, transparent 100%),
      radial-gradient(ellipse 140px 200px at 90px 220px, var(--photo-skin) 0%, #4a4a4a 55%, var(--photo-dark) 100%);
    border-right: 2px solid #555;
  }
  .banner__claim, .banner__guarantee {
    position: absolute; left: 7px;
    font-family: "Arimo", sans-serif; font-weight: 700;
    font-size: 11px; color: var(--label); white-space: nowrap;
  }
  .banner__claim { top: 6px; }
  .banner__guarantee { bottom: 7px; font-size: 10.5px; }

  .banner__panel {
    flex: 1; height: 100%; min-width: 0;
    background: linear-gradient(180deg, var(--panel-top) 0%, #f1f1f1 45%, var(--panel-bottom) 100%);
    display: flex; flex-direction: column; align-items: center; justify-content: center;
    font-family: "Encode Sans Condensed", sans-serif; color: var(--teal);
    text-transform: uppercase; text-align: center; line-height: 0.95;
    white-space: nowrap;
  }

  .headline-small { font-size: 34px; font-weight: 400; }
  .headline-large { font-size: 74px; font-weight: 400; letter-spacing: -1px; }
  .banner--question .headline-small { margin-bottom: 6px; }
  .banner--statement .headline-small { font-size: 46px; }
  .banner--statement .headline-large { font-size: 86px; }

  .banner--offer .banner__panel { justify-content: flex-start; padding-top: 10px; }
  .banner--offer .headline-small { font-size: 48px; }
  .banner--offer .headline-large { font-size: 74px; }

  .benefit-title {
    margin-top: 12px; font-size: 24px; font-weight: 700; color: var(--teal-dark);
    align-self: flex-start; padding-left: 10px;
  }
  .benefit-list { list-style: none; align-self: flex-start; padding-left: 8px; margin-top: 8px; }
  .benefit-list li {
    display: flex; align-items: center; gap: 4px;
    font-family: "Arimo", sans-serif; font-weight: 700; font-size: 10px;
    color: var(--teal-dark); line-height: 1; margin-bottom: 10px; white-space: nowrap;
  }
  .benefit-list em { font-style: italic; text-transform: none; font-size: 11px; text-decoration: underline; }
  .tick { width: 13px; height: 13px; flex: none; }

  .cta {
    margin-top: 8px; width: 156px; height: 30px;
    background: linear-gradient(180deg, var(--button-top), var(--button-bottom));
    border: 1px solid #c9650a; border-radius: 3px;
    color: var(--button-text); font-family: "Arimo", sans-serif; font-weight: 700;
    font-size: 14px; display: flex; align-items: center; justify-content: center;
    text-decoration: none;
  }
</style>
</head>
<body>
<main class="canvas">

  <section class="banner banner--question">
    <div class="banner__photo" role="img" aria-label="Close-up photo of a hand holding a sore knee with a red glow over the joint">
      <span class="banner__claim">Backed by Clinical Studies</span>
    </div>
    <div class="banner__panel">
      <span class="headline-small">Do you have</span>
      <span class="headline-large">Joint</span>
      <span class="headline-large">Pain?</span>
    </div>
  </section>

  <section class="banner banner--statement">
    <div class="banner__photo" role="img" aria-label="Close-up photo of a hand holding a sore knee with a red glow over the joint">
      <span class="banner__claim">Backed by Clinical Studies</span>
    </div>
    <div class="banner__panel">
      <span class="headline-small">No more</span>
      <span class="headline-large">Pain</span>
    </div>
  </section>

  <section class="banner banner--offer">
    <div class="banner__photo" role="img" aria-label="Close-up photo of a hand holding a sore knee with a red glow over the joint">
      <span class="banner__claim">Backed by Clinical Studies</span>
      <span class="banner__guarantee">100% Satisfaction Guarantee</span>
    </div>
    <div class="banner__panel">
      <span class="headline-small">No more</span>
      <span class="headline-large">Pain</span>
      <span class="benefit-title">Reduce joint</span>
      <ul class="benefit-list">
        <li><svg class="tick" viewBox="0 0 14 14"><path d="M1 7.5 L5 11.5 L13 2" fill="none" stroke="var(--teal)" stroke-width="2.6" stroke-linecap="round" stroke-linejoin="round"/></svg>STIFFNESS IN 10 DAYS&nbsp;<em>or less</em></li>
        <li><svg class="tick" viewBox="0 0 14 14"><path d="M1 7.5 L5 11.5 L13 2" fill="none" stroke="var(--teal)" stroke-width="2.6" stroke-linecap="round" stroke-linejoin="round"/></svg>PAIN IN 7 DAYS&nbsp;<em>or less</em></li>
      </ul>
      <a class="cta" href="#">LEARN MORE</a>
    </div>
  </section>

</main>
</body>
</html>
```